Building company needs a new logo and letterhead design

We need a new and refreshed logo and letterhead design for an existing building company. We specialise in residential as well as commercial building/construction, design and project management. Our company name is Talvek Constructions Pty Ltd. Our primary colours that we want to use are black/orange/white. We do renovations/alterations/new homes both residential and commercial. We are a medium sized building company. We want something simple and modern.

Industry/Entity Type

Residential

```html
<!DOCTYPE html>
<html lang="en">
<head>
<meta charset="utf-8">
<title>Talvek Constructions Pty Ltd – Letterhead</title>
<link rel="stylesheet" href="https://fonts.googleapis.com/css2?family=PT+Serif&display=swap">
<style>
  :root {
    --paper: #ffffff;
    --brand-orange: #dc8332;
    --brand-orange-soft: #f0b47a;
    --brand-orange-pale: #fbe6d2;
    --ink: #2b2b2b;
  }
  html, body {
    margin: 0;
    padding: 0;
    overflow: hidden;
    background: var(--paper);
  }
  .letterhead {
    position: relative;
    width: 873px;
    height: 1200px;
    background: var(--paper);
    overflow: hidden;
    font-family: "PT Serif", Georgia, serif;
  }
  .header-rule-lead {
    position: absolute;
    left: 0;
    top: 141px;
    width: 42px;
    height: 11px;
    background: linear-gradient(to right, var(--paper), var(--brand-orange-pale));
  }
  .header-rule {
    position: absolute;
    left: 148px;
    top: 141px;
    right: 0;
    height: 11px;
    background: var(--brand-orange);
  }
  .brand-square {
    position: absolute;
    left: 42px;
    top: 58px;
    width: 106px;
    height: 107px;
    background: linear-gradient(to right, var(--brand-orange-pale), var(--brand-orange-soft) 55%, var(--brand-orange));
    box-shadow: 1px 1px 3px rgba(0, 0, 0, 0.18);
  }
  .brand-name {
    position: absolute;
    left: 154px;
    top: 84px;
    margin: 0;
    color: var(--brand-orange);
    font-weight: 400;
    line-height: 1;
  }
  .brand-name-main {
    display: block;
    font-size: 38px;
    letter-spacing: 0.5px;
  }
  .brand-name-sub {
    display: block;
    margin-top: 4px;
    font-size: 13px;
  }
</style>
</head>
<body>
  <main class="letterhead">
    <div class="header-rule-lead"></div>
    <div class="header-rule"></div>
    <div class="brand-square"></div>
    <h1 class="brand-name">
      <span class="brand-name-main">TALVEK</span>
      <span class="brand-name-sub">Constructions Pty Ltd.</span>
    </h1>
  </main>
</body>
</html>
```